Association Insurance WhitePaper

Need white paper layout design for cover page, data pages and back page, much like a powerpoint design. Looking for similar designs as the uploaded drawing style.

```html
<!DOCTYPE html>
<html lang="en">
<head>
<meta charset="utf-8">
<title>Association Insurance White Paper – Slide Set</title>
<link href="https://fonts.googleapis.com/css2?family=Plus+Jakarta+Sans:wght@400;500;600;700&display=swap" rel="stylesheet">
<style>
:root{
  --ink:#1c1c1c;
  --body:#3a3a3a;
  --sky:#5bc3e0;
  --ocean:#1fa6d0;
  --mist:#eaf6fa;
  --grey:#d6d6d6;
  --grey-soft:#ececec;
  --backdrop:#165e77;
  --white:#ffffff;
}
*{box-sizing:border-box;margin:0;padding:0}
html,body{width:1200px;height:1008px;overflow:hidden;background:var(--backdrop)}
body{font-family:"Plus Jakarta Sans",sans-serif;color:var(--ink)}
.deck{position:relative;width:1200px;height:1008px;overflow:hidden}
.slide{position:absolute;width:634px;height:356px;background:var(--white);overflow:hidden;transform:scale(.5714);transform-origin:0 0}
.slide .abs{position:absolute}
.has-bar::after{content:"";position:absolute;left:0;right:0;bottom:0;height:10px;background:linear-gradient(to right,var(--sky) 50%,var(--ocean) 50%)}
.c1{left:39.4px}.c2{left:418.9px}.c3{left:798.3px}
.r1{top:49.7px}.r2{top:284.6px}.r3{top:519.4px}.r4{top:754.3px}

.brand{position:absolute;display:flex;align-items:center;gap:5px}
.brand-mark{width:17px;height:17px;border:1.5px solid var(--ocean)}
.brand-name{font-size:6px;font-weight:600;line-height:1.05;letter-spacing:.3px;text-transform:uppercase;color:var(--ink)}
.topbar .brand{left:30px;top:12px}
.topbar-line{position:absolute;left:104px;right:30px;top:22px;height:1px;background:var(--grey-soft)}
.brand.big .brand-mark{width:22px;height:22px}
.brand.big .brand-name{font-size:8.5px}

.title-blue{position:absolute;left:0;right:0;text-align:center;font-size:22px;font-weight:600;color:var(--sky)}
.lead{position:absolute;left:0;right:0;text-align:center;font-size:6.5px;line-height:1.7;color:var(--body)}
.small{font-size:6.5px;line-height:1.65;color:var(--body)}
.photo{position:absolute}

/* cover */
.cover-art{position:absolute;inset:0;background:
  linear-gradient(to bottom,rgba(255,255,255,1) 28%,rgba(255,255,255,0) 55%),
  linear-gradient(100deg,#e9b9d4 0%,#f2dca0 30%,#b9dde9 55%,#cfe6ee 80%,#d8d0e6 100%)}
.cover-title{position:absolute;left:42px;top:70px;font-size:29px;font-weight:700;line-height:1.25}

/* agenda */
.agenda-pill{position:absolute;left:0;top:55px;width:195px;height:50px;background:var(--sky);border-radius:0 25px 25px 0;color:var(--white);font-size:30px;font-weight:600;display:flex;align-items:center;justify-content:center}
.agenda-item{position:absolute;left:338px;width:240px}
.agenda-item h3{font-size:13px;font-weight:500;color:var(--sky);margin-bottom:4px}
.agenda-item p{padding-left:15px}

/* mission */
.mission-title{position:absolute;left:0;right:0;top:62px;text-align:center;font-size:23px;font-weight:600}
.mission-card{position:absolute;top:153px;width:169px;height:145px;background:var(--sky);color:var(--white);text-align:center}
.mission-card .rule{position:absolute;left:16px;right:16px;top:58px;height:1px;background:rgba(255,255,255,.55)}
.mission-card h3{position:absolute;left:0;right:0;top:72px;font-size:14px;font-weight:600}
.mission-card p{position:absolute;left:20px;right:20px;top:95px;font-size:6.5px;line-height:1.65;color:#eaf8fc}
.mission-card svg{position:absolute;left:74px;top:20px}

/* data list */
.data-panel{position:absolute;left:0;top:95px;width:207px;height:208px;background:var(--mist)}
.num-item{position:absolute;left:36px;display:flex;gap:10px}
.num-box{width:22px;height:22px;background:var(--sky);color:var(--white);font-size:11px;display:flex;align-items:center;justify-content:center;flex:none}
.num-item h3{font-size:12px;font-weight:500;color:var(--sky);margin-bottom:2px}

/* team */
.member{position:absolute;top:145px;width:104px;text-align:center}
.member .band{height:43px}
.member .avatar{position:absolute;left:24px;top:14px;width:56px;height:56px;border-radius:50%;border:3px solid var(--white)}
.member h3{margin-top:42px;font-size:13px;font-weight:500;color:var(--sky)}
.member p{font-size:5.8px;line-height:1.6;color:var(--body)}

/* lists */
.bullet{position:absolute;left:62px;display:flex;gap:14px;align-items:flex-start}
.bullet .dot{width:28px;height:28px;border-radius:50%;flex:none;display:flex;align-items:center;justify-content:center}
.bullet h3{font-size:11px;font-weight:600;margin-bottom:1px}
.contact{position:absolute;left:330px;display:flex;gap:16px;font-size:9px;line-height:1.4}
</style>
</head>
<body>
<main class="deck">

<!-- 1 Cover -->
<section class="slide c1 r1">
  <div class="cover-art" role="img" aria-label="Watercolor sketch of a city skyline with towers and rail lines"></div>
  <div class="brand big" style="left:40px;top:25px"><span class="brand-mark"></span><span class="brand-name">Harbor<br>Mutual<br>Cover</span></div>
  <h1 class="cover-title">Community Whitepaper<br>Headline Here</h1>
</section>

<!-- 2 Agenda -->
<section class="slide c2 r1 has-bar">
  <div class="agenda-pill">Agenda</div>
  <div class="photo" style="left:85px;top:120px;width:225px;height:186px;background:linear-gradient(135deg,#e4e4e4,#c9c9c9)" role="img" aria-label="Hand signing an insurance claim form on a clipboard"></div>
  <div class="agenda-item" style="top:98px"><h3>1. Headline Here</h3><p class="small">Lorem ipsum dolor sit amet dummy texts. Duis quis amet nunc vulputate dolor. Scelerisque ligula faucibus.</p></div>
  <div class="agenda-item" style="top:156px"><h3>2. Headline Here</h3><p class="small">Lorem ipsum dolor sit amet dummy texts. Duis quis amet nunc vulputate dolor. Scelerisque ligula faucibus.</p></div>
  <div class="agenda-item" style="top:214px"><h3>3. Headline Here</h3><p class="small">Lorem ipsum dolor sit amet dummy texts. Duis quis amet nunc vulputate dolor. Scelerisque ligula faucibus.</p></div>
  <div class="agenda-item" style="top:267px"><h3>4. Headline Here</h3><p class="small">Lorem ipsum dolor sit amet dummy texts. Duis quis amet nunc vulputate dolor. Scelerisque ligula faucibus.</p></div>
</section>

<!-- 3 Mission -->
<section class="slide c3 r1 has-bar">
  <div class="topbar"><div class="brand"><span class="brand-mark"></span><span class="brand-name">Harbor<br>Mutual<br>Cover</span></div><div class="topbar-line"></div></div>
  <h2 class="mission-title">Our Mission</h2>
  <p class="lead" style="top:98px">Lorem ipsum dolor sit amet dummy texts. Duis quis amet nunc<br>vulputate dolor. Scelerisque ligula faucibus.</p>
  <div class="mission-card" style="left:52px"><svg width="22" height="22" viewBox="0 0 22 22"><circle cx="11" cy="6" r="4" fill="#fff"/><path d="M3 20c0-5 4-8 8-8s8 3 8 8z" fill="#fff"/></svg><div class="rule"></div><h3>Headline Here</h3><p>Lorem ipsum dolor sit amet dummy texts. Duis quis amet nunc vulputate dolor scelerisque ligula</p></div>
  <div class="mission-card" style="left:232px"><svg width="22" height="22" viewBox="0 0 22 22"><circle cx="6" cy="5" r="3" fill="#fff"/><circle cx="11" cy="4" r="3" fill="#fff"/><circle cx="16" cy="5" r="3" fill="#fff"/><path d="M3 20v-6h16v6z" fill="#fff"/></svg><div class="rule"></div><h3>Headline Here</h3><p>Lorem ipsum dolor sit amet dummy texts. Duis quis amet nunc vulputate dolor scelerisque ligula</p></div>
  <div class="mission-card" style="left:412px"><svg width="22" height="22" viewBox="0 0 22 22"><path d="M2 18l7-7 4 3 7-8" stroke="#fff" stroke-width="2.5" fill="none"/><path d="M15 5h6v6" stroke="#fff" stroke-width="2.5" fill="none"/></svg><div class="rule"></div><h3>Headline Here</h3><p>Lorem ipsum dolor sit amet dummy texts. Duis quis amet nunc vulputate dolor scelerisque ligula</p></div>
</section>

<!-- 4 Bar chart -->
<section class="slide c1 r2 has-bar">
  <div class="topbar"><div class="brand"><span class="brand-mark"></span><span class="brand-name">Harbor<br>Mutual<br>Cover</span></div><div class="topbar-line"></div></div>
  <h2 class="title-blue" style="left:36px;right:auto;top:52px">Headline Goes Here</h2>
  <div class="data-panel"></div>
  <div class="num-item" style="top:118px"><span class="num-box">1</span><div><h3>Headline Here</h3><p class="small">Lorem ipsum dolor sit amet dummy<br>texts. Duis quis amet nunc</p></div></div>
  <div class="num-item" style="top:184px"><span class="num-box">2</span><div><h3>Headline Here</h3><p class="small">Lorem ipsum dolor sit amet dummy<br>texts. Duis quis amet nunc</p></div></div>
  <div class="num-item" style="top:250px"><span class="num-box">3</span><div><h3>Headline Here</h3><p class="small">Lorem ipsum dolor sit amet dummy<br>texts. Duis quis amet nunc</p></div></div>
  <svg class="abs" style="left:0;top:0" width="634" height="356" viewBox="0 0 634 356" font-family="Plus Jakarta Sans, sans-serif" font-size="6.5" fill="#5bc3e0" text-anchor="middle">
    <line x1="228" y1="277" x2="600" y2="277" stroke="#e2e2e2"/>
    <g>
      <rect x="248" y="128" width="10" height="149" fill="#5bc3e0"/><text x="253" y="124">43%</text>
      <rect x="266" y="194" width="10" height="83" fill="#1fa6d0"/><text x="271" y="190">24%</text>
      <rect x="284" y="208" width="10" height="69" fill="#d6d6d6"/><text x="289" y="204">20%</text>
      <rect x="342" y="190" width="10" height="87" fill="#5bc3e0"/><text x="347" y="186">25%</text>
      <rect x="360" y="124" width="10" height="153" fill="#1fa6d0"/><text x="365" y="120">44%</text>
      <rect x="378" y="208" width="10" height="69" fill="#d6d6d6"/><text x="383" y="204">20%</text>
      <rect x="436" y="156" width="10" height="121" fill="#5bc3e0"/><text x="441" y="152">35%</text>
      <rect x="454" y="214" width="10" height="63" fill="#1fa6d0"/><text x="459" y="210">18%</text>
      <rect x="472" y="173" width="10" height="104" fill="#d6d6d6"/><text x="477" y="169">30%</text>
      <rect x="530" y="121" width="10" height="156" fill="#5bc3e0"/><text x="535" y="117">45%</text>
      <rect x="548" y="180" width="10" height="97" fill="#1fa6d0"/><text x="553" y="176">28%</text>
      <rect x="566" y="104" width="10" height="173" fill="#d6d6d6"/><text x="571" y="100">50%</text>
    </g>
    <g fill="#3a3a3a" text-anchor="start" font-size="6">
      <rect x="348" y="292" width="5" height="5" fill="#5bc3e0"/><text x="356" y="297">Data 1</text>
      <rect x="392" y="292" width="5" height="5" fill="#a8a8a8"/><text x="400" y="297">Data 1</text>
      <rect x="437" y="292" width="5" height="5" fill="#d6d6d6"/><text x="445" y="297">Data 1</text>
    </g>
  </svg>
</section>

<!-- 5 Rings -->
<section class="slide c2 r2 has-bar">
  <div class="topbar"><div class="brand"><span class="brand-mark"></span><span class="brand-name">Harbor<br>Mutual<br>Cover</span></div><div class="topbar-line"></div></div>
  <h2 class="title-blue" style="top:54px">Headline Goes Here</h2>
  <p class="lead" style="top:90px">Lorem ipsum dolor sit amet dummy texts. Duis quis amet nunc<br>vulputate dolor. Scelerisque ligula faucibus.</p>
  <svg class="abs" style="left:0;top:0" width="634" height="356" viewBox="0 0 634 356" font-family="Plus Jakarta Sans, sans-serif" font-size="17" font-weight="500" fill="#5bc3e0" text-anchor="middle">
    <g fill="none" stroke-width="9">
      <circle cx="153" cy="198" r="52" stroke="#ececec"/>
      <circle cx="153" cy="198" r="52" stroke="#5bc3e0" stroke-dasharray="196 131" transform="rotate(-90 153 198)"/>
      <circle cx="317" cy="198" r="52" stroke="#ececec"/>
      <circle cx="317" cy="198" r="52" stroke="#1fa6d0" stroke-dasharray="245 82" transform="rotate(-90 317 198)"/>
      <circle cx="483" cy="198" r="52" stroke="#f2f2f2"/>
      <circle cx="483" cy="198" r="52" stroke="#d6d6d6" stroke-dasharray="147 180" transform="rotate(-90 483 198)"/>
    </g>
    <text x="153" y="204">60%</text><text x="317" y="204" fill="#1fa6d0">75%</text><text x="483" y="204">45%</text>
  </svg>
  <p class="small abs" style="left:88px;width:130px;top:272px;text-align:center">Lorem ipsum dolor sit amet dummy texts. Duis quis amet nunc vulputate dolor scelerisque ligula</p>
  <p class="small abs" style="left:252px;width:130px;top:272px;text-align:center">Lorem ipsum dolor sit amet dummy texts. Duis quis amet nunc vulputate dolor scelerisque ligula</p>
  <p class="small abs" style="left:418px;width:130px;top:272px;text-align:center">Lorem ipsum dolor sit amet dummy texts. Duis quis amet nunc vulputate dolor scelerisque ligula</p>
</section>

<!-- 6 Timeline -->
<section class="slide c3 r2 has-bar">
  <div class="topbar"><div class="brand"><span class="brand-mark"></span><span class="brand-name">Harbor<br>Mutual<br>Cover</span></div><div class="topbar-line"></div></div>
  <h2 class="title-blue" style="top:44px">Timeline Area</h2>
  <svg class="abs" style="left:0;top:0" width="634" height="356" viewBox="0 0 634 356" font-family="Plus Jakarta Sans, sans-serif" fill="#fff" text-anchor="middle">
    <line x1="89" y1="189" x2="545" y2="189" stroke="#5bc3e0"/>
    <g stroke="#5bc3e0"><line x1="165" y1="165" x2="165" y2="189"/><line x1="317" y1="165" x2="317" y2="189"/><line x1="469" y1="165" x2="469" y2="189"/><line x1="241" y1="189" x2="241" y2="216"/><line x1="393" y1="189" x2="393" y2="216"/></g>
    <g fill="#5bc3e0"><circle cx="165" cy="189" r="2"/><circle cx="241" cy="189" r="2"/><circle cx="317" cy="189" r="2"/><circle cx="393" cy="189" r="2"/><circle cx="469" cy="189" r="2"/></g>
    <circle cx="89" cy="189" r="35" fill="#1fa6d0"/><circle cx="165" cy="130" r="35" fill="#5bc3e0"/><circle cx="241" cy="251" r="35" fill="#5bc3e0"/><circle cx="317" cy="130" r="35" fill="#1fa6d0"/><circle cx="393" cy="251" r="35" fill="#5bc3e0"/><circle cx="469" cy="130" r="35" fill="#5bc3e0"/><circle cx="545" cy="189" r="35" fill="#1fa6d0"/>
    <g font-size="12" font-weight="600"><text x="89" y="186">2015</text><text x="165" y="127">2017</text><text x="241" y="248">2019</text><text x="317" y="127">2021</text><text x="393" y="248">2023</text><text x="469" y="127">2025</text><text x="545" y="186">2027</text></g>
    <g font-size="5" fill="#e8f7fc"><text x="89" y="196">Lorem ipsum</text><text x="89" y="203">dolor amet</text><text x="165" y="137">Lorem ipsum</text><text x="165" y="144">dolor amet</text><text x="241" y="258">Lorem ipsum</text><text x="241" y="265">dolor amet</text><text x="317" y="137">Lorem ipsum</text><text x="317" y="144">dolor amet</text><text x="393" y="258">Lorem ipsum</text><text x="393" y="265">dolor amet</text><text x="469" y="137">Lorem ipsum</text><text x="469" y="144">dolor amet</text><text x="545" y="196">Lorem ipsum</text><text x="545" y="203">dolor amet</text></g>
  </svg>
  <div class="abs" style="left:37px;top:254px;width:130px"><h3 style="font-size:12px;font-weight:500;color:var(--sky);margin-bottom:2px">Headline Here</h3><p class="small">Lorem ipsum dolor sit amet dummy texts. Duis quis amet nunc vulputate dolor scelerisque ligula</p></div>
  <div class="abs" style="right:37px;top:254px;width:130px;text-align:right"><h3 style="font-size:12px;font-weight:500;color:var(--sky);margin-bottom:2px">Headline Here</h3><p class="small">Lorem ipsum dolor sit amet dummy texts. Duis quis amet nunc vulputate dolor scelerisque ligula</p></div>
</section>

<!-- 7 Workflow -->
<section class="slide c1 r3 has-bar">
  <div class="topbar"><div class="brand"><span class="brand-mark"></span><span class="brand-name">Harbor<br>Mutual<br>Cover</span></div><div class="topbar-line"></div></div>
  <h2 class="title-blue" style="top:62px">Workflow Area</h2>
  <p class="lead" style="top:98px">Lorem ipsum dolor sit amet dummy texts. Duis quis amet nunc<br>vulputate dolor. Scelerisque ligula faucibus.</p>
  <svg class="abs" style="left:0;top:0" width="634" height="356" viewBox="0 0 634 356" font-family="Plus Jakarta Sans, sans-serif" text-anchor="middle">
    <g fill="none" stroke-width="21">
      <path d="M58 216 A53 53 0 0 1 164 216" stroke="#5bc3e0"/>
      <path d="M162 216 A53 53 0 0 0 268 216" stroke="#1fa6d0"/>
      <path d="M266 216 A53 53 0 0 1 372 216" stroke="#5bc3e0"/>
      <path d="M370 216 A53 53 0 0 0 476 216" stroke="#1fa6d0"/>
      <path d="M474 216 A53 53 0 0 1 580 216" stroke="#5bc3e0"/>
    </g>
    <g font-size="7" fill="#fff">
      <circle cx="111" cy="199" r="10" fill="#5bc3e0"/><text x="111" y="202">1</text>
      <circle cx="215" cy="228" r="10" fill="#1fa6d0"/><text x="215" y="231">2</text>
      <circle cx="319" cy="199" r="10" fill="#5bc3e0"/><text x="319" y="202">3</text>
      <circle cx="423" cy="228" r="10" fill="#1fa6d0"/><text x="423" y="231">4</text>
      <circle cx="527" cy="199" r="10" fill="#5bc3e0"/><text x="527" y="202">5</text>
    </g>
    <g font-size="10" fill="#5bc3e0"><text x="111" y="227">Data 1</text><text x="215" y="162">Data 2</text><text x="319" y="227">Data 3</text><text x="423" y="162">Data 4</text><text x="527" y="227">Data 5</text></g>
  </svg>
  <p class="abs" style="left:71px;top:233px;width:80px;text-align:center;font-size:5px;line-height:1.6;color:var(--body)">Lorem ipsum dolor sit amet dummy texts. Duis quis amet nunc vulputate dolor scelerisque ligula.</p>
  <p class="abs" style="left:175px;top:168px;width:80px;text-align:center;font-size:5px;line-height:1.6;color:var(--body)">Lorem ipsum dolor sit amet dummy texts. Duis quis amet nunc vulputate dolor scelerisque ligula.</p>
  <p class="abs" style="left:279px;top:233px;width:80px;text-align:center;font-size:5px;line-height:1.6;color:var(--body)">Lorem ipsum dolor sit amet dummy texts. Duis quis amet nunc vulputate dolor scelerisque ligula.</p>
  <p class="abs" style="left:383px;top:168px;width:80px;text-align:center;font-size:5px;line-height:1.6;color:var(--body)">Lorem ipsum dolor sit amet dummy texts. Duis quis amet nunc vulputate dolor scelerisque ligula.</p>
  <p class="abs" style="left:487px;top:233px;width:80px;text-align:center;font-size:5px;line-height:1.6;color:var(--body)">Lorem ipsum dolor sit amet dummy texts. Duis quis amet nunc vulputate dolor scelerisque ligula.</p>
</section>

<!-- 8 Team -->
<section class="slide c2 r3 has-bar">
  <div class="topbar"><div class="brand"><span class="brand-mark"></span><span class="brand-name">Harbor<br>Mutual<br>Cover</span></div><div class="topbar-line"></div></div>
  <h2 class="title-blue" style="top:62px">Team Headline</h2>
  <p class="lead" style="top:98px">Lorem ipsum dolor sit amet dummy texts. Duis quis amet nunc<br>vulputate dolor. Scelerisque ligula faucibus.</p>
  <div class="member" style="left:60px"><div class="band" style="background:var(--sky)"></div><div class="avatar" style="background:#c9b8aa" role="img" aria-label="Portrait of a team member"></div><h3>Dana Whitfield</h3><p>Lorem ipsum dolor sit amet dummy texts. Duis quis amet nunc vulputate dolor scelerisque ligula</p><p style="margin-top:8px">Ph: 555 010 7890<br>Em: dana@harborcover.example</p></div>
  <div class="member" style="left:197px"><div class="band" style="background:var(--ocean)"></div><div class="avatar" style="background:#d9b0b8" role="img" aria-label="Portrait of a team member"></div><h3>Dana Whitfield</h3><p>Lorem ipsum dolor sit amet dummy texts. Duis quis amet nunc vulputate dolor scelerisque ligula</p><p style="margin-top:8px">Ph: 555 010 7890<br>Em: dana@harborcover.example</p></div>
  <div class="member" style="left:334px"><div class="band" style="background:var(--sky)"></div><div class="avatar" style="background:#a9a29c" role="img" aria-label="Portrait of a team member"></div><h3>Dana Whitfield</h3><p>Lorem ipsum dolor sit amet dummy texts. Duis quis amet nunc vulputate dolor scelerisque ligula</p><p style="margin-top:8px">Ph: 555 010 7890<br>Em: dana@harborcover.example</p></div>
  <div class="member" style="left:470px"><div class="band" style="background:var(--ocean)"></div><div class="avatar" style="background:#cdbfb4" role="img" aria-label="Portrait of a team member"></div><h3>Dana Whitfield</h3><p>Lorem ipsum dolor sit amet dummy texts. Duis quis amet nunc vulputate dolor scelerisque ligula</p><p style="margin-top:8px">Ph: 555 010 7890<br>Em: dana@harborcover.example</p></div>
</section>

<!-- 9 Arc hub -->
<section class="slide c3 r3">
  <div class="topbar"><div class="brand"><span class="brand-mark"></span><span class="brand-name">Harbor<br>Mutual<br>Cover</span></div><div class="topbar-line"></div></div>
  <h2 class="title-blue" style="top:54px">Headline Goes Here</h2>
  <svg class="abs" style="left:0;top:0" width="634" height="356" viewBox="0 0 634 356" font-family="Plus Jakarta Sans, sans-serif" text-anchor="middle">
    <path d="M150 356 A167 167 0 0 1 484 356" fill="none" stroke="#5bc3e0" stroke-dasharray="3 3"/>
    <g fill="#fff" stroke="#5bc3e0" stroke-width="2"><circle cx="317" cy="203" r="4"/><circle cx="226" cy="227" r="4"/><circle cx="408" cy="227" r="4"/><circle cx="170" cy="287" r="4"/><circle cx="464" cy="287" r="4"/></g>
    <path d="M193 356 A124 124 0 0 1 441 356 Z" fill="#1fa6d0"/>
    <text x="317" y="302" font-size="19" font-weight="600" fill="#fff">Headline</text>
    <text x="317" y="324" font-size="19" font-weight="600" fill="#fff">Goes Here</text>
    <g fill="#5bc3e0" stroke="#eaf6fa" stroke-width="5">
      <circle cx="113" cy="287" r="26"/><circle cx="197" cy="198" r="26"/><circle cx="317" cy="162" r="26"/><circle cx="436" cy="198" r="26"/><circle cx="521" cy="287" r="26"/>
    </g>
    <g fill="#fff">
      <path d="M113 277l8 3v6c0 5-4 8-8 10-4-2-8-5-8-10v-6z"/>
      <rect x="187" y="195" width="20" height="9" rx="2"/><circle cx="192" cy="206" r="2.5"/><circle cx="202" cy="206" r="2.5"/>
      <path d="M305 164l12-10 12 10v10h-24z"/>
      <path d="M436 207c-9-6-11-10-11-13a5 5 0 0 1 11-2 5 5 0 0 1 11 2c0 3-2 7-11 13z"/>
      <circle cx="521" cy="281" r="5"/><path d="M510 296c0-6 5-9 11-9s11 3 11 9z"/>
    </g>
    <g font-size="10" fill="#5bc3e0">
      <text x="113" y="244">Headline</text><text x="113" y="255">Goes Here</text>
      <text x="197" y="156">Headline</text><text x="197" y="167">Goes Here</text>
      <text x="317" y="120">Headline</text><text x="317" y="131">Goes Here</text>
      <text x="436" y="156">Headline</text><text x="436" y="167">Goes Here</text>
      <text x="521" y="244">Headline</text><text x="521" y="255">Goes Here</text>
    </g>
  </svg>
</section>

<!-- 10 Feature -->
<section class="slide c1 r4">
  <div class="topbar"><div class="brand"><span class="brand-mark"></span><span class="brand-name">Harbor<br>Mutual<br>Cover</span></div><div class="topbar-line"></div></div>
  <div class="photo" style="left:0;top:44px;width:137px;height:134px;background:linear-gradient(160deg,#6f8f5c,#c9d6c0)" role="img" aria-label="Paper cut-out family under an umbrella held in a hand"></div>
  <div class="photo" style="left:137px;top:44px;width:137px;height:134px;background:linear-gradient(160deg,#8d8a86,#dcd6cf)" role="img" aria-label="Hand holding an umbrella over a small model house"></div>
  <h2 class="abs" style="left:291px;top:34px;font-size:22.5px;font-weight:700;line-height:1.2">Protecting the<br>Association from<br>Lawsuits</h2>
  <p class="small abs" style="left:291px;top:124px;width:260px">Lorem ipsum dolor sit amet dummy texts. Duis quis amet nunc vulputate dolor. Scelerisque ligula faucibus.</p>
  <div class="photo" style="left:274px;top:178px;width:360px;height:178px;background:linear-gradient(120deg,#b99b86,#e4ddd6 60%,#c8c8c8)" role="img" aria-label="Agent meeting a smiling couple at a desk"></div>
  <div class="abs" style="left:25px;top:186px;width:100px"><h3 style="font-size:10px;font-weight:500;color:var(--sky);line-height:1.25;margin-bottom:10px">Key Coverages Every Association Needs</h3><p style="font-size:5.8px;line-height:1.65;color:var(--body)">Lorem ipsum dolor sit amet dummy texts. Duis quis amet nunc vulputate dolor. Scelerisque ligula velit nulla faucibus donec pellentesque massa mi. Aliquam in fusce semper aliquam egestas.</p></div>
  <div class="abs" style="left:143px;top:186px;width:105px"><h3 style="font-size:10px;font-weight:500;color:var(--sky);line-height:1.25;margin-bottom:10px">Protecting Common Areas and Structures</h3><p style="font-size:5.8px;line-height:1.65;color:var(--body)">Lorem ipsum dolor sit amet dummy texts. Duis quis amet nunc vulputate dolor. Scelerisque ligula velit nulla faucibus donec pellentesque massa mi. Aliquam in fusce semper aliquam egestas.</p></div>
</section>

<!-- 11 Bullets and donut -->
<section class="slide c2 r4 has-bar">
  <div class="topbar"><div class="brand"><span class="brand-mark"></span><span class="brand-name">Harbor<br>Mutual<br>Cover</span></div><div class="topbar-line"></div></div>
  <h2 class="title-blue" style="top:44px">Bullet &amp; Chart Area</h2>
  <div class="bullet" style="top:116px"><span class="dot" style="background:var(--sky)"><svg width="10" height="10" viewBox="0 0 10 10"><circle cx="4" cy="4" r="3" stroke="#fff" fill="none" stroke-width="1.5"/><line x1="6" y1="6" x2="9" y2="9" stroke="#fff" stroke-width="1.5"/></svg></span><div><h3>Headline Here</h3><p class="small" style="font-size:6px">Lorem ipsum dolor sit amet dummy texts. Duis quis<br>amet nunc vulputate dolor scelerisque ligula.</p></div></div>
  <div class="bullet" style="top:168px"><span class="dot" style="background:#9fa8b4"><svg width="10" height="10" viewBox="0 0 10 10"><circle cx="5" cy="3" r="2.3" fill="#fff"/><path d="M1 10c0-3 2-4.5 4-4.5s4 1.5 4 4.5z" fill="#fff"/></svg></span><div><h3>Headline Here</h3><p class="small" style="font-size:6px">Lorem ipsum dolor sit amet dummy texts. Duis quis<br>amet nunc vulputate dolor scelerisque ligula.</p></div></div>
  <div class="bullet" style="top:221px"><span class="dot" style="background:var(--sky)"><svg width="10" height="10" viewBox="0 0 10 10"><path d="M1 5l8-4-3 8-1-3z" fill="#fff"/></svg></span><div><h3>Headline Here</h3><p class="small" style="font-size:6px">Lorem ipsum dolor sit amet dummy texts. Duis quis<br>amet nunc vulputate dolor scelerisque ligula.</p></div></div>
  <div class="bullet" style="top:275px"><span class="dot" style="background:#9fa8b4"><svg width="10" height="10" viewBox="0 0 10 10"><path d="M1 9l3-5 2 3 1-2 2 4z" fill="#fff"/></svg></span><div><h3>Headline Here</h3><p class="small" style="font-size:6px">Lorem ipsum dolor sit amet dummy texts. Duis quis<br>amet nunc vulputate dolor scelerisque ligula.</p></div></div>
  <svg class="abs" style="left:0;top:0" width="634" height="356" viewBox="0 0 634 356" font-family="Plus Jakarta Sans, sans-serif" font-size="15" fill="#5bc3e0" text-anchor="middle">
    <g fill="none" stroke-width="22" transform="rotate(-90 460 211)">
      <circle cx="460" cy="211" r="66" stroke="#5bc3e0" stroke-dasharray="248.8 414.7"/>
      <circle cx="460" cy="211" r="66" stroke="#1fa6d0" stroke-dasharray="103.7 414.7" stroke-dashoffset="-248.8"/>
      <circle cx="460" cy="211" r="66" stroke="#bdbdbd" stroke-dasharray="62.2 414.7" stroke-dashoffset="-352.5"/>
      <circle cx="460" cy="211" r="66" stroke="#d9d9d9" stroke-dasharray="41.5 414.7" stroke-dashoffset="-414.7"/>
    </g>
    <g fill="#5bc3e0"><rect x="447" y="214" width="5" height="12"/><rect x="455" y="208" width="5" height="18"/><rect x="463" y="212" width="5" height="14"/><rect x="471" y="203" width="5" height="23"/><path d="M446 210l10-8 7 5 12-11" stroke="#5bc3e0" stroke-width="2" fill="none"/></g>
    <text x="420" y="123">10%</text><text x="362" y="175">15%</text><text x="568" y="213">60%</text><text x="360" y="261">25%</text>
    <g font-size="6" fill="#3a3a3a" text-anchor="start">
      <rect x="393" y="307" width="5" height="5" fill="#5bc3e0"/><text x="400" y="312">Data</text>
      <rect x="414" y="307" width="5" height="5" fill="#1fa6d0"/><text x="421" y="312">Data</text>
      <rect x="435" y="307" width="5" height="5" fill="#bdbdbd"/><text x="442" y="312">Data</text>
      <rect x="456" y="307" width="5" height="5" fill="#d9d9d9"/><text x="463" y="312">Data</text>
    </g>
  </svg>
</section>

<!-- 12 Thank you -->
<section class="slide c3 r4">
  <div class="photo" style="left:0;top:53px;width:297px;height:251px;background:linear-gradient(120deg,#cfc2b2,#e9e2d9 55%,#9b8f85)" role="img" aria-label="Smiling couple shaking hands with an insurance agent on a sofa"></div>
  <div class="brand big" style="left:330px;top:64px"><span class="brand-mark"></span><span class="brand-name">Harbor<br>Mutual<br>Cover</span></div>
  <h2 class="abs" style="left:330px;top:118px;font-size:27px;font-weight:600">Thank you</h2>
  <div class="contact" style="top:172px"><svg width="10" height="10" viewBox="0 0 10 10"><path d="M2 1l2 2-1 1.5a6 6 0 0 0 2.5 2.5L7 6l2 2-1.5 1.5C4 9 1 6 .5 2.5z" fill="#5bc3e0"/></svg><span>+123 456 7890<br>+123 456 7890</span></div>
  <div class="contact" style="top:210px"><svg width="10" height="10" viewBox="0 0 10 10"><path d="M1 5l8-4-3 8-1-3z" fill="#5bc3e0"/></svg><span>hello@harborcover.example<br>www.harborcover.example</span></div>
  <div class="contact" style="top:245px"><svg width="10" height="10" viewBox="0 0 10 10"><path d="M5 1l4.5 4H8v4H2V5H.5z" fill="#5bc3e0"/></svg><span>1234 Street name, town/city<br>State/Country, Post 1234</span></div>
</section>

</main>
</body>
</html>
```